Our soon to be released website will provide information on any drink and eat deals or other "themed" (recurring) events worth mentioning.
Visitors will be able to find the place they are looking for using tags, location,prices, timings and services.
Examples are: Ladies Night, Brunches, Happy Hour, Iftar, Business Lunch, Hotelier Night, etc.
Launching city = Dubai

Target Market(s)

Visitors of bars, clubs, lounges and restaurants in Dubai

Industry/Entity Type

Events

Contact Information for Business Card

Velvet Hour and Feasts Dubai
Maurits de Klerven
Founder
T +971 (0)50 - 314 2086
E maurits@VvelvetHourandFeastsDubai.example
I www.VelvetHourandFeastsDubai.example
Facebook /velvethourandfeastsdubai
Instagram /velvethour_feasts_dubai/
P.O. Box 347620, Dubai, United Arab Emirates (or) UAE
100% Velvet Hour & Feasts
100% Up-to-date
100% Searchable

Logo Text

Velvet Hour & Feasts (not the word Dubai)

Requirements
Must have
• Business cards should make clear that our company:
• - can attract more visitors for clubs, restaurants, bars etc.
Nice to have
• The website name will be: www.velvethourandfeastsdubai.example
• (and that's also the name of this project).
• We purely decided for this name so everybody knows what we offer (up to date and extensive infromation about recurring drink and eat deals) and it should help us as well in SEO.

```html
<!DOCTYPE html>
<html lang="en">
<head>
<meta charset="utf-8">
<title>Velvet Hour and Feasts Dubai — Business Card</title>
<link rel="stylesheet" href="https://fonts.googleapis.com/css2?family=Share+Tech+Mono&family=Cousine&display=swap">
<style>
  :root {
    --backdrop: #95ada0;
    --card-top: #0a1020;
    --card-mid: #050a18;
    --card-bottom: #0b1322;
    --band-core: #8fd0ff;
    --band-blue: #2f6bff;
    --band-glow: rgba(60, 120, 255, 0.35);
    --dust: rgba(90, 80, 220, 0.35);
    --art-violet: rgba(150, 110, 210, 0.55);
    --art-blue: rgba(60, 150, 220, 0.5);
    --text-light: #f4f6ff;
    --text-dark: #141a2c;
    --panel: rgba(255, 255, 255, 0.84);
    --rule: rgba(255, 255, 255, 0.85);
  }
  * { margin: 0; padding: 0; box-sizing: border-box; }
  html, body {
    width: 1200px; height: 616px; overflow: hidden;
    background: var(--backdrop);
  }
  .canvas { position: relative; width: 1200px; height: 616px; }
  .card {
    position: absolute; top: 145px;
    width: 540px; height: 326px;
    border-radius: 16px; overflow: hidden;
    background: linear-gradient(180deg, var(--card-top) 0%, var(--card-mid) 45%, var(--card-bottom) 100%);
  }
  .card--back { left: 40px; }
  .card--front { left: 620px; }

  .light-band {
    position: absolute; left: 0; right: 0; top: 146px; height: 34px;
    background: linear-gradient(180deg, transparent 0%, var(--band-glow) 25%, var(--band-blue) 45%, var(--band-core) 50%, var(--band-blue) 55%, var(--band-glow) 75%, transparent 100%);
    opacity: 0.9;
  }
  .dust-haze {
    position: absolute; left: 40%; right: 0; top: 205px; height: 60px;
    background: radial-gradient(ellipse at 60% 50%, var(--dust) 0%, transparent 70%);
  }

  .site-url {
    position: absolute;
    font-family: "Share Tech Mono", monospace;
    letter-spacing: 1.5px;
    white-space: nowrap;
  }
  .card--back .site-url {
    left: 13px; top: 104px;
    font-size: 22px; color: var(--text-light);
  }

  .contact-block {
    position: absolute; left: 10px; top: 266px;
    font-family: "Cousine", monospace;
    font-size: 9.2px; line-height: 12.5px;
    color: var(--text-light);
    border-left: 1px solid var(--rule);
    padding-left: 5px;
  }
  .contact-block p { white-space: nowrap; position: relative; }
  .contact-block p::before {
    content: ""; position: absolute; left: -5px; top: 6px;
    width: 4px; border-top: 1px solid var(--rule);
  }

  .art-area {
    position: absolute; left: 0; top: 86px;
    width: 285px; height: 160px;
    border-radius: 10px;
    background: linear-gradient(180deg, var(--art-violet) 0%, var(--art-blue) 100%);
  }

  .tagline {
    position: absolute; left: 314px; top: 86px;
    font-family: "Share Tech Mono", monospace;
    font-size: 12px; line-height: 14px; letter-spacing: 1px;
    color: var(--text-light);
    padding-bottom: 4px;
    width: 206px;
    border-bottom: 2px solid var(--rule);
  }

  .url-panel {
    position: absolute; left: 16px; top: 132px;
    width: 508px; height: 48px;
    border-radius: 8px;
    background: var(--panel);
  }
  .card--front .site-url {
    left: 28px; top: 143px;
    font-size: 21px; color: var(--text-dark);
  }
  .panel-rule {
    position: absolute; left: 0; top: 192px;
    width: 224px; height: 2px;
    background: var(--rule);
  }
</style>
</head>
<body>
<main class="canvas">

  <section class="card card--back" aria-label="Business card back">
    <div class="light-band" role="img" aria-label="Glowing blue light band with hexagon pattern"></div>
    <div class="dust-haze" role="img" aria-label="Faint violet sparkle dust"></div>
    <p class="site-url">www.velvethourandfeastsdubai.example</p>
    <div class="contact-block">
      <p>Velvet Hour and Feasts Dubai Maurits de Klerven Founder T +971 (0)50 - 314 2086</p>
      <p>E maurits@VvelvetHourandFeastsDubai.example I</p>
      <p>www.VelvetHourandFeastsDubai.example Facebook /velvethourandfeastsdubai</p>
      <p>Instagram /velvethour_feasts_dubai/ P.O. Box 347620, Dubai, United Arab</p>
    </div>
  </section>

  <section class="card card--front" aria-label="Business card front">
    <div class="light-band" role="img" aria-label="Glowing blue light band with hexagon pattern"></div>
    <div class="dust-haze" role="img" aria-label="Faint violet sparkle dust"></div>
    <div class="art-area" role="img" aria-label="Colourful flowers and butterfly illustration"></div>
    <p class="tagline">more visitors for venues<br>look at here</p>
    <div class="url-panel"></div>
    <p class="site-url">www.velvethourandfeastsdubai.example</p>
    <div class="panel-rule"></div>
  </section>

</main>
</body>
</html>
```